Nobre Lente Lusitana - business card

Create a business card for my eyewear (glasses) store. The concept is based in handcrafted glasses (as well as common frames and 3d printed), clean, and elegant. The business card could be black (white letters and symbols) or white (black letters and symbols) but we are open to new suggestions. It must be sober and elegant.
The name Nobre Lente Lusitana means Royal/Real Portuguese Optical Store.
Our concept should be inspired by the pictures attatched bellow.
I would like it to be classic and elegant as business cards for bankers.
Our first selected logo is also available in attachment files.

Target Market(s)

For business meetings with investors, supliers and fairs

Industry/Entity Type

Eyewear

Contact Information for Business Card

Some random business cards in attachment that we like. Don't be closed to it, we like freedom of think.

Font styles to use
Serif
Sans Serif

Colors
404040
e9e9e9
fbfbfb
000000
85abd3
0255a3
f7fbfd
959595

Requirements
Must have
• Must be elegant, simple.
• Must present our brand new logo (slight variations are welcome, the logo is not closed yet). See our temporary logo in attachment.
• Black (or dark grey), white (or light grey) and a third slight color.
• This third slight color could be dark blue or grayish blue.
• Info:
• Tomás Vidigal (name)
• tvidigal@nobrelentelusitana.example
• +351 927364051
• www.nobrelentelusitana.example
Nice to have
• Black and white or with serious colors such as dark blue or greyish blue.
• Could also have water mark with our logo (big size) in the background (inspired in KMT bank credit card design)
Should not have
• Hysteric colora or shapes

```html
<!DOCTYPE html>
<html lang="pt">
<head>
<meta charset="utf-8">
<title>Nobre Lente Lusitana – Cartão de visita</title>
<link rel="stylesheet" href="https://fonts.googleapis.com/css2?family=Arvo&family=Lato:wght@400&family=Arimo&display=swap">
<style>
  :root {
    --backdrop: #9b9b9b;
    --ink: #000000;
    --paper: #ffffff;
    --shadow: rgba(0, 0, 0, 0.45);
  }
  html, body {
    margin: 0;
    padding: 0;
    overflow: hidden;
  }
  body {
    width: 1200px;
    height: 900px;
    background: var(--backdrop);
    position: relative;
  }
  .card {
    position: absolute;
    top: 306px;
    height: 272px;
    border-radius: 10px;
    overflow: hidden;
    box-shadow: 2px 3px 4px var(--shadow);
  }
  .card--front {
    left: 150px;
    width: 438px;
    background: var(--paper);
  }
  .card--back {
    left: 608px;
    width: 441px;
    background: var(--ink);
  }
  .brand-panel {
    position: absolute;
    left: 0;
    top: 0;
    width: 166px;
    height: 100%;
    background: var(--ink);
  }
  .brand-name {
    position: absolute;
    left: 0;
    right: 0;
    text-align: center;
    font-family: "Arvo", serif;
    font-weight: 400;
    color: var(--paper);
    font-size: 17px;
    line-height: 30px;
    letter-spacing: 5px;
    text-transform: uppercase;
  }
  .brand-panel .brand-name { top: 74px; padding-left: 5px; }
  .card--back .brand-name { top: 74px; padding-left: 5px; }
  .brand-name span { display: block; }
  .holder {
    position: absolute;
    left: 186px;
    top: 96px;
    margin: 0;
    font-family: "Arvo", serif;
    font-weight: 400;
    font-size: 14px;
    letter-spacing: 0.3px;
    color: var(--ink);
    text-transform: uppercase;
  }
  .contact {
    position: absolute;
    left: 186px;
    top: 140px;
    margin: 0;
    padding: 0;
    list-style: none;
    font-family: "Lato", sans-serif;
    font-size: 12.5px;
    line-height: 16px;
    color: var(--ink);
  }
  .contact li {
    display: flex;
    align-items: center;
    gap: 4px;
  }
  .contact svg { width: 9px; height: 9px; flex: none; }
  .web-address {
    position: absolute;
    left: 0;
    right: 0;
    top: 223px;
    text-align: center;
    font-family: "Arimo", sans-serif;
    font-size: 11.5px;
    letter-spacing: 1.2px;
    color: var(--paper);
  }
</style>
</head>
<body>
  <section class="card card--front" aria-label="Frente do cartão">
    <div class="brand-panel">
      <div class="brand-name"><span>Nobre</span><span>Lente</span><span>Lusitana</span></div>
    </div>
    <h1 class="holder">Tomás Vidigal</h1>
    <ul class="contact">
      <li>
        <svg viewBox="0 0 10 10" aria-hidden="true"><rect x="0.5" y="1.5" width="9" height="7" fill="#000"/><path d="M0.8 2 L5 5.4 L9.2 2" stroke="#fff" stroke-width="1" fill="none"/></svg>
        tvidigal@nobrelentelusitana.example
      </li>
      <li>
        <svg viewBox="0 0 10 10" aria-hidden="true"><circle cx="5" cy="5" r="4.5" fill="#000"/><path d="M2.5 3.2 Q4 2.5 4.6 4 Q5.5 5 4.2 6.5 M6.2 2 Q7.5 4 6.8 6.2 Q7.8 7 7 8" stroke="#fff" stroke-width="0.9" fill="none"/></svg>
        www.nobrelentelusitana.example
      </li>
    </ul>
  </section>

  <section class="card card--back" aria-label="Verso do cartão">
    <div class="brand-name"><span>Nobre</span><span>Lente</span><span>Lusitana</span></div>
    <p class="web-address">www.nobrelentelusitana.example</p>
  </section>
</body>
</html>
```